Accommodation business card design

We need a business card designed for our long-term accommodation business based in Australia. The business card must match the style of the attached letterhead and logo. The same contact details that are on the letterhead will also go on the card except that the card must list the contact details in the following order:phone, email, home address, ABN.

The card will be printed on .76mm white pvc plastic (same as credit cards), printed both sides and will be silver foil stamped on at least one side (preferably 2 sides) The design template is attached, but please go to www.qz-cardworks.com.au for more specs.

The only other addition the card will be my name: Dalwyn Prothero

Industry/Entity Type

Accommodation

```html
<!DOCTYPE html>
<html lang="en">
<head>
<meta charset="utf-8">
<title>Kestrel Lodging – Business Card</title>
<link href="https://fonts.googleapis.com/css2?family=Open+Sans:ital,wght@0,400;0,700;0,800;1,400&display=swap" rel="stylesheet">
<style>
  :root {
    --maroon: #6d1a3b;
    --clay: #8d4b46;
    --ink: #3a3a3a;
    --muted: #666;
    --card: #ffffff;
    --backdrop: #ebe7e3;
  }
  * { box-sizing: border-box; margin: 0; padding: 0; }
  html, body { width: 1200px; height: 847px; overflow: hidden; }
  body {
    background: var(--backdrop);
    font-family: "Open Sans", Arial, sans-serif;
    position: relative;
  }
  .card {
    position: absolute;
    top: 260px;
    width: 520px;
    height: 328px;
    background: var(--card);
    border-radius: 16px;
    overflow: hidden;
    box-shadow: 0 4px 14px rgba(0,0,0,.12);
  }
  .card--front { left: 40px; }
  .card--back { left: 640px; }
  .card__swoosh { position: absolute; inset: 0; width: 100%; height: 100%; overflow: hidden; }
  .brand {
    position: absolute;
    display: flex;
    align-items: center;
    gap: 10px;
  }
  .brand__mark {
    width: 44px; height: 40px;
    background: var(--maroon);
    border-radius: 6px;
  }
  .brand__name {
    color: var(--maroon);
    font-weight: 800;
    font-size: 19px;
    line-height: 1.05;
    letter-spacing: .5px;
    text-transform: uppercase;
  }
  .card--front .brand { left: 50%; top: 50%; transform: translate(-50%, -62%); }
  .card--back .brand { left: 48px; top: 30px; }
  .holder {
    position: absolute;
    right: 40px;
    top: 38px;
    text-align: right;
  }
  .holder__name { color: var(--muted); font-size: 15px; }
  .holder__role { color: var(--maroon); font-size: 12px; font-style: italic; }
  .contacts {
    position: absolute;
    left: 60px;
    top: 130px;
    list-style: none;
    font-size: 13px;
    color: var(--ink);
  }
  .contacts li { display: flex; align-items: flex-start; gap: 8px; margin-bottom: 5px; line-height: 1.2; }
  .contacts svg { width: 14px; height: 14px; flex: none; margin-top: 1px; }
  .contacts .abn { padding-left: 22px; color: var(--maroon); }
</style>
</head>
<body>

<section class="card card--front" aria-label="Card front">
  <svg class="card__swoosh" viewBox="0 0 520 328" preserveAspectRatio="none" aria-hidden="true">
    <path d="M0 52 Q60 4 175 0 L200 0 Q70 8 14 60 Z" fill="var(--maroon)"/>
    <path d="M300 328 Q400 275 520 238 L520 252 Q410 288 330 328 Z" fill="var(--maroon)"/>
    <path d="M370 328 Q450 292 520 272 L520 300 Q470 312 420 328 Z" fill="var(--clay)"/>
  </svg>
  <div class="brand">
    <span class="brand__mark"></span>
    <span class="brand__name">Kestrel<br>Lodging</span>
  </div>
</section>

<section class="card card--back" aria-label="Card back">
  <svg class="card__swoosh" viewBox="0 0 520 328" preserveAspectRatio="none" aria-hidden="true">
    <path d="M-14 40 Q-34 235 68 340 L92 340 Q-6 235 10 60 Z" fill="var(--maroon)"/>
    <path d="M300 328 Q400 268 520 232 L520 246 Q410 282 330 328 Z" fill="var(--maroon)"/>
    <path d="M368 328 Q450 290 520 268 L520 296 Q470 310 420 328 Z" fill="var(--clay)"/>
  </svg>
  <div class="brand">
    <span class="brand__mark"></span>
    <span class="brand__name">Kestrel<br>Lodging</span>
  </div>
  <div class="holder">
    <p class="holder__name">Dalwyn Prothero</p>
    <p class="holder__role">CEO</p>
  </div>
  <ul class="contacts">
    <li>
      <svg viewBox="0 0 14 14" aria-hidden="true"><circle cx="7" cy="7" r="7" fill="var(--maroon)"/><path d="M5 4c-1 1 0 4 2.5 5.5 1.5 1 2.5.8 3-.2L9 8 8 8.7 5.8 6.2 6.4 5Z" fill="#fff"/></svg>
      <span>0400 555 208</span>
    </li>
    <li>
      <svg viewBox="0 0 14 14" aria-hidden="true"><circle cx="7" cy="7" r="7" fill="var(--maroon)"/><rect x="3.5" y="4.5" width="7" height="5" fill="#fff"/><path d="M3.5 4.5 7 7.5 10.5 4.5" fill="none" stroke="var(--maroon)" stroke-width=".9"/></svg>
      <span>dalwyn.prothero@kestrelmail.com</span>
    </li>
    <li>
      <svg viewBox="0 0 14 14" aria-hidden="true"><circle cx="7" cy="7" r="7" fill="var(--maroon)"/><path d="M3.5 7.5 7 4.5 10.5 7.5 M4.8 7v3h4.4V7" fill="none" stroke="#fff" stroke-width="1.2"/></svg>
      <span>PO Box 3816, Harlow Mail Centre<br>QLD 4902</span>
    </li>
    <li class="abn">ABN 51 804 227 913</li>
  </ul>
</section>

</body>
</html>
```